Jewelry Shop Needs a Business Card Design

***We want a very sharp and unforgettable pantone for the Business Card. ***
***We do not want the business card or logo only in black, white and grey color!!!Please provide us a main color as our brand topic! Thanks!! ***

Mabel’s Nook is a Hong Kong based fine jewelry brand.

We want a very nice, simple and elegant business card design for Mabel's Nook Brand. The company's logo has been uploaded already.

You can design with below info:

Dorian Fung
Director
M: +852 94273658
T: +852 35820417
F: +852 35820419
E: dorian.fung@mabelsnook.example
5/F , Harbourlight Tower, 12-18 Orchid Lane, Wan Tung Kok, Kowloon, Hong Kong

Target Market(s)

Mabel’s Nook philosophy is a jewelry icon of young, creative, trendy, fashionable, stylish, energetic, and elegant. For Mabel’s Nook, jewelry is one collection of artworks, the most important items in personal life.

Industry/Entity Type

Jewelry

Requirements
Must have
• We want a very sharp and unforgettable pantone for the Business Card.

```html
<!DOCTYPE html>
<html lang="en">
<head>
<meta charset="utf-8">
<title>Mabel’s Nook – Business Card</title>
<link rel="stylesheet" href="https://fonts.googleapis.com/css2?family=Cinzel:wght@400;600&family=Didact+Gothic&display=swap">
<style>
  :root {
    --page: #1a1a1a;
    --brand: #a3134f;
    --brand-deep: #6e0a33;
    --brand-light: #c2366f;
    --card-front: #ffffff;
    --card-front-shade: #f1ecee;
    --ink: #2b2b2b;
    --ink-soft: #555555;
    --mark: #fbf3f6;
  }
  * { margin: 0; padding: 0; box-sizing: border-box; }
  html, body {
    width: 1200px; height: 675px; overflow: hidden;
    background: var(--page);
  }
  .canvas {
    width: 1200px; height: 675px;
    display: flex; align-items: center; justify-content: center; gap: 60px;
  }
  .card {
    width: 510px; height: 292px;
    border-radius: 2px;
    box-shadow: 0 12px 30px rgba(0,0,0,.55);
    position: relative;
    overflow: hidden;
  }
  .card-back {
    background: linear-gradient(160deg, var(--brand-light), var(--brand) 45%, var(--brand-deep));
    display: flex; flex-direction: column; align-items: center; justify-content: center; gap: 18px;
  }
  .brand-dot {
    width: 86px; height: 86px; border-radius: 50%;
    background: var(--mark);
  }
  .brand-name {
    font-family: "Cinzel", serif; font-weight: 400;
    font-size: 22px; letter-spacing: 1.5px;
    color: var(--mark);
  }
  .card-front {
    background: linear-gradient(135deg, var(--card-front) 40%, var(--card-front-shade));
    color: var(--ink);
    display: flex; flex-direction: column; align-items: center;
    padding-top: 62px;
  }
  .card-front::after {
    content: ""; position: absolute; left: 0; right: 0; bottom: 0;
    height: 8px; background: var(--brand);
  }
  .person-name {
    font-family: "Cinzel", serif; font-weight: 600;
    font-size: 26px; letter-spacing: 1.5px;
    color: var(--brand);
  }
  .person-title {
    font-family: "Didact Gothic", sans-serif; font-weight: 400;
    font-size: 15px; color: var(--ink-soft); margin-top: 2px;
  }
  .address {
    font-family: "Didact Gothic", sans-serif;
    font-size: 10.5px; line-height: 1.6; text-align: center;
    color: var(--ink-soft); margin-top: 38px;
  }
  .contacts {
    font-family: "Didact Gothic", sans-serif;
    font-size: 10.5px; color: var(--ink-soft);
    display: grid; grid-template-columns: auto auto; column-gap: 28px; row-gap: 4px;
    margin-top: 16px;
  }
  .contact-label { font-weight: 700; color: var(--brand); margin-right: 10px; }
</style>
</head>
<body>
  <main class="canvas">
    <section class="card card-back" aria-label="Card back">
      <div class="brand-dot"></div>
      <div class="brand-name">Mabel’s Nook</div>
    </section>
    <section class="card card-front" aria-label="Card front">
      <h1 class="person-name">Dorian Fung</h1>
      <p class="person-title">Director</p>
      <p class="address">5/F , Harbourlight Tower, 12-18 Orchid Lane<br>Wan Tung Kok, Kowloon Hong Kong</p>
      <div class="contacts">
        <span><span class="contact-label">M</span>+852 94273658</span>
        <span><span class="contact-label">T</span>+852 35820417</span>
        <span><span class="contact-label">F</span>+852 35820419</span>
        <span><span class="contact-label">E</span>dorian.fung@mabelsnook.example</span>
      </div>
    </section>
  </main>
</body>
</html>
```